Quillbase Design Project - App Review

Take a look at this website, gridvault.example. We are creating something very similar to this, four pages are required. The name of our website is BrightPickDigest.example
1) The home page which highlights, app of the day, a carousel which highlights featured apps, and top apps in different categories
2) Single App Page - This page will details the app that is selected, app icon, app description, app ratings, and other information you can find on an app page in the lumora market
3) A page that list all the apps in a category, for example if the user select, "100 top apps" the page that will display the list of 100 apps, 10 per page, summary of description, a small icon, screenshot etc for each app
4) Review Page - where we review an app of the day, including screenshots, videos, text reviews etc
I do not have any logo at the moment, use these as nav links; home, my apps, reviews, blog and contact. Thank you.
I will like to see a nice creativity. I am open to a very beautiful color combinations. Thank you
Target Market(s)
App shoppers, people that are looking for new apps, discounted apps etc
Industry/Entity Type
Store
Look and feel

```html
<!DOCTYPE html>
<html lang="en">
<head>
<meta charset="utf-8">
<title>App Review</title>
<link rel="stylesheet" href="https://fonts.googleapis.com/css2?family=Arimo:wght@400;700&display=swap">
<style>
:root{
  --bg:#eceef0;
  --panel:#ffffff;
  --blue:#1b3f9b;
  --ink:#333333;
  --muted:#555a60;
  --line:#dcdfe2;
  --card:#f1f2f3;
  --card-foot:#d8d9db;
  --dot:#9fd0ea;
  --gold:#f0a81c;
  --star-off:#b9b2a2;
  --footer:#dce1e8;
}
*{box-sizing:border-box;margin:0;padding:0}
html,body{width:1059px;height:1200px;overflow:hidden}
body{background:radial-gradient(ellipse at 50% 0,#f5f6f7 0,var(--bg) 60%);font-family:"Arimo",Arial,sans-serif;color:var(--ink);position:relative}
.abs{position:absolute}
.logo{left:94px;top:49px;width:200px;height:65px;background:linear-gradient(#fafafa,#e3e4e6);border-radius:4px;box-shadow:0 2px 3px rgba(0,0,0,.12);display:flex;align-items:center;justify-content:center;font-weight:700;font-size:29px;letter-spacing:-1px;color:#2d2d2d}
.logo span{color:var(--blue)}
.search{left:799px;top:75px;width:168px;height:31px;background:#fff;border:1px solid var(--line);font-size:10px;color:#999;padding:10px 12px}
.search svg{position:absolute;right:10px;top:8px}
.nav{left:85px;top:135px;width:882px;height:45px;background:var(--panel);border-radius:4px 4px 0 0;border-bottom:2px solid var(--line);display:flex}
.nav a{display:flex;align-items:center;padding:0 14px 0 28px;font-size:11.5px;color:var(--blue);text-decoration:none;border-right:1px solid var(--line);letter-spacing:-.3px}
.nav a:last-child{border-right:none}
.hero{left:85px;top:187px;width:882px;height:273px;background:var(--panel);border-bottom:2px solid var(--line)}
.hero h1{position:absolute;left:36px;top:28px;font-size:43px;color:var(--blue);letter-spacing:-2px;font-weight:700}
.hero .lead{position:absolute;left:43px;top:118px;width:360px;font-size:11px;line-height:13px;color:#222;font-weight:700}
.hero .body{position:absolute;left:45px;top:145px;width:362px;font-size:11px;line-height:13.5px;color:var(--muted)}
.hero .more{position:absolute;left:44px;top:207px;font-size:11.5px;color:var(--blue);font-weight:700}
.shot{left:429px;top:71px;width:214px;height:132px;background:linear-gradient(160deg,#1a1a1a 0,#c7651e 35%,#8a3c12 55%,#222 75%)}
.app-icon{left:662px;top:56px;width:163px;height:163px;border-radius:30px;background:linear-gradient(#3a3a3a,#0d0d0d);display:flex;align-items:center;justify-content:center;color:#fff;font-size:22px;font-weight:700}
.dots{left:413px;top:248px;display:flex;gap:9px}
.dots i{width:10px;height:10px;border-radius:50%;background:var(--dot);display:block}
.top{left:85px;top:484px;width:882px;height:276px;background:var(--panel)}
.sec-title{font-size:16px;color:var(--blue);font-weight:700;letter-spacing:.2px}
.top .sec-title{position:absolute;left:36px;top:25px}
.choose{position:absolute;left:545px;top:21px;font-size:13px;color:var(--blue);font-weight:700}
.select{position:absolute;left:665px;top:14px;width:169px;height:31px;border:1px solid var(--line);font-size:10px;color:#888;padding:10px 14px}
.select svg{position:absolute;right:10px;top:11px}
.card{top:80px;width:271px;height:145px;background:var(--card);border-bottom:3px solid var(--line)}
.card h3{position:absolute;left:18px;top:36px;width:150px;font-size:13.5px;line-height:16px;color:var(--blue);font-weight:700}
.card p{position:absolute;left:18px;top:82px;width:245px;font-size:11px;line-height:13.7px;color:var(--muted);white-space:nowrap}
.card .ico{position:absolute;right:16px;top:39px;width:67px;height:67px;border-radius:10px;display:flex;align-items:center;justify-content:center;color:#fff;font-size:9.5px;font-weight:700;text-align:center}
.stars{font-size:12px;color:var(--star-off)}
.stars b{color:var(--gold);font-weight:400}
.card .stars{position:absolute;right:14px;top:14px}
.card .foot{position:absolute;left:0;top:145px;width:271px;height:27px;background:var(--card-foot);display:flex;justify-content:space-between;padding:7px 22px;font-size:11.5px;color:var(--blue);font-weight:700}
.rule{left:85px;top:772px;width:882px;height:1px;background:var(--line)}
.recent-title{left:0;width:1145px;top:787px;text-align:center}
.arrows{left:913px;top:799px}
.entry{top:823px;width:182px;height:240px;background:var(--panel);text-align:center}
.entry .ico{width:110px;height:110px;margin:15px auto 0;display:flex;align-items:center;justify-content:center;color:#fff;font-weight:700;font-size:13px}
.entry h4{margin-top:10px;font-size:16px;color:var(--blue);font-weight:700}
.entry p{margin:10px auto 0;width:160px;font-size:10.5px;line-height:13px;color:#3d3d3d}
.entry .stars{margin-top:6px;font-size:12px;color:#a9a08c;letter-spacing:1px}
.footer{left:85px;top:1085px;width:882px;height:115px;background:var(--footer)}
.footer nav{position:absolute;left:40px;top:38px;display:flex}
.footer nav a{font-size:11.5px;color:var(--blue);text-decoration:none;margin-right:27px;letter-spacing:-.3px}
.footer .legal{position:absolute;left:40px;top:63px;font-size:10.5px;line-height:13px;color:#8a9099}
.social{position:absolute;right:30px;top:32px;display:flex;gap:8px;align-items:center}
.social span{display:flex;align-items:center;gap:3px;font-size:9.5px;color:var(--blue);font-weight:700}
.social i{width:10px;height:10px;border-radius:50%;display:block}
</style>
</head>
<body>

<div class="abs logo">App&nbsp;<span>Review</span></div>
<div class="abs search">Search
  <svg width="14" height="14" viewBox="0 0 14 14"><circle cx="5.5" cy="5.5" r="4.3" fill="none" stroke="#aaa" stroke-width="1.6"/><line x1="8.6" y1="8.6" x2="13" y2="13" stroke="#aaa" stroke-width="2"/></svg>
</div>

<nav class="abs nav">
  <a href="#">HOME</a><a href="#">MY APPS</a><a href="#">REVIEWS</a><a href="#">BLOG</a><a href="#">CONTACT</a>
</nav>

<section class="abs hero">
  <h1>APP OF THE DAY</h1>
  <p class="lead">Encora streams the widest selection of the highest quality concert films and music documentaries to any digital device worldwide.</p>
  <p class="body">Encora offers a wide range of All-Access features such as: premium and curated content, design your own Setlists, Share, social concert digital premiers, unlimited viewing on every Encora application, live Q&amp;A sessions with artists, monthly reviews from tastemakers, and more.</p>
  <a class="more">Read Full Review</a>
  <div class="abs shot" role="img" aria-label="App screenshot showing Sunvale Fest concert banner and a row of album covers"></div>
  <div class="abs app-icon">Encora</div>
  <div class="abs dots"><i></i><i></i><i></i><i></i></div>
</section>

<section class="abs top">
  <h2 class="sec-title">TOP APPS THIS WEEK</h2>
  <span class="choose">Choose category</span>
  <div class="select">Arts &amp; Entertainment
    <svg width="10" height="8" viewBox="0 0 10 8"><path d="M0 0h10L5 8z" fill="#bbb"/></svg>
  </div>

  <article class="abs card" style="left:17px">
    <span class="stars"><b>★★★★</b>★</span>
    <h3>RouteRider GPS Cycling Riding</h3>
    <div class="ico" style="background:#c4242c">RouteRider</div>
    <p>Turn your phone into the<br>ultimate cycling computer.<br>Easily track route, speed,<br>distance, calories, time with much more!</p>
    <div class="foot"><span>Read Review</span><span>Adventure Sports</span></div>
  </article>
  <article class="abs card" style="left:301px">
    <span class="stars" style="top:8px"><b>★★★</b>★★</span>
    <h3 style="top:28px">RouteRider GPS Cycling Riding</h3>
    <div class="ico" style="background:#1c7fd0;top:30px">Sonarly</div>
    <p>Turn your phone into the<br>ultimate cycling computer.<br>Easily track route, speed,<br>distance, calories, time with much more!</p>
  </article>
  <article class="abs card" style="left:584px">
    <span class="stars" style="top:12px"><b>★★★</b>★★</span>
    <h3 style="top:33px">RouteRider GPS Cycling Riding</h3>
    <div class="ico" style="background:#4fae2e;top:35px;height:65px">Notewell</div>
    <p>Turn your phone into the<br>ultimate cycling computer.<br>Easily track route, speed,<br>distance, calories, time with much more!</p>
  </article>
</section>

<div class="abs rule"></div>
<h2 class="abs sec-title recent-title">RECENT ENTRIES TO THE MARKET</h2>
<svg class="abs arrows" width="18" height="8" viewBox="0 0 18 8"><path d="M6 0v8L0 4z M12 0v8l6-4z" fill="#222"/></svg>

<article class="abs entry" style="left:114px">
  <div class="ico" style="background:linear-gradient(#ffb21a,#f08a0a);border-radius:14px">TuneTracker</div>
  <h4>TuneTracker</h4>
  <p>Lorem ipsum dolor sit amet, consectetur adipisicing elit, sed do eiusmod tempor incididunt</p>
  <div class="stars">★★★★★</div>
</article>
<article class="abs entry" style="left:327px">
  <div class="ico" role="img" aria-label="Shopping app artwork with a shopping bag" style="background:linear-gradient(135deg,#b48ad8,#6d3fa0);border-radius:6px"></div>
  <h4>Shopping App</h4>
  <p>Lorem ipsum dolor sit amet, consectetur adipisicing elit, sed do eiusmod tempor incididunt</p>
  <div class="stars">★★★★★</div>
</article>
<article class="abs entry" style="left:539px">
  <div class="ico" style="background:#1a1a1a;border-radius:50%">Sipsy</div>
  <h4>Sipsy App</h4>
  <p>Lorem ipsum dolor sit amet, consectetur adipisicing elit, sed do eiusmod tempor incididunt</p>
  <div class="stars">★★★★★</div>
</article>
<article class="abs entry" style="left:752px">
  <div class="ico" style="background:#f4511e">Pacely</div>
  <h4>Pacely G</h4>
  <p>Lorem ipsum dolor sit amet, consectetur adipisicing elit, sed do eiusmod tempor incididunt</p>
  <div class="stars">★★★★★</div>
</article>

<footer class="abs footer">
  <nav><a href="#">HOME</a><a href="#">MY APPS</a><a href="#">REVIEWS</a><a href="#">BLOG</a><a href="#">CONTACT</a></nav>
  <p class="legal">Copyright 2013. All rights reserved.<br>Terms &amp; Conditions &nbsp;- &nbsp;Privacy &nbsp;- &nbsp;Disclaimer</p>
  <div class="social">
    <span><i style="background:#3b5a9a"></i>Linkly</span>
    <span><i style="background:#d9363e"></i>Clipora</span>
    <span><i style="background:#41a8e0"></i>Pingo</span>
  </div>
</footer>

</body>
</html>
```